Company or website name
- Harwood & Beale LLP
- Links to the website
- harwoodbeale-example.com
- Describe your company and organization and target audience
- lawyers and clients in the need of lawyer for defective products etc
- The design should have the following
- yes
- Other Facts

```html
<!DOCTYPE html>
<html lang="en">
<head>
<meta charset="utf-8">
<title>Harwood &amp; Beale LLP</title>
<link rel="stylesheet" href="https://fonts.googleapis.com/css2?family=Arimo:wght@400;700&family=Cinzel:wght@500&display=swap">
<style>
  :root {
    --navy: #0b2a6b;
    --navy-text: #0d2a72;
    --white: #ffffff;
    --grey-line: #a9a9a9;
    --grey-text: #444444;
    --footer-bg: #4b4e53;
    --footer-text: #8e9196;
    --pill-border: #ffffff;
  }
  * { box-sizing: border-box; margin: 0; padding: 0; }
  html, body { width: 961px; height: 1200px; overflow: hidden; }
  body {
    font-family: "Arimo", Arial, sans-serif;
    background: linear-gradient(90deg, #0a1d4d 0%, var(--navy) 3%, var(--navy) 97%, #0a1d4d 100%);
    position: relative;
  }
  .page {
    position: absolute; left: 42px; top: 0; width: 871px; height: 1200px;
    background: var(--white);
  }
  /* header */
  .site-header { position: absolute; left: 0; top: 0; width: 871px; height: 86px; border-top: 3px solid #cfcfcf; }
  .brand {
    position: absolute; left: 22px; top: 32px; white-space: nowrap;
    font-family: "Cinzel", Georgia, serif; font-size: 17px; color: var(--navy-text); letter-spacing: .2px;
  }
  .main-nav { position: absolute; left: 0; top: 0; width: 871px; height: 86px; }
  .main-nav a {
    position: absolute; top: 34px; font-weight: 700; font-size: 17px; color: var(--navy-text);
    text-decoration: none; padding-bottom: 5px; border-bottom: 5px solid var(--grey-line);
    text-align: center; white-space: nowrap;
  }
  .main-nav a.current { font-size: 20px; top: 32px; border-bottom-color: var(--navy); }
  .band { position: absolute; left: 0; width: 871px; background: var(--navy); }
  /* hero */
  .portrait {
    position: absolute; left: 124px; top: 100px; width: 123px; height: 242px;
    background: linear-gradient(180deg, #f3f3f3 0%, #2a2a30 30%, #1c1c22 100%);
    border-radius: 50px 50px 6px 6px;
  }
  .hero-banner {
    position: absolute; left: 270px; top: 119px; width: 484px; height: 177px;
    background: linear-gradient(180deg, #e9e9ea, #dcdcde);
    display: flex; align-items: center; justify-content: center; white-space: nowrap;
    font-family: "Cinzel", Georgia, serif; font-size: 38px; color: var(--navy-text);
  }
  .tagline { position: absolute; left: 64px; top: 357px; font-size: 17px; font-weight: 700; color: var(--grey-text); }
  .intro { position: absolute; left: 68px; top: 390px; width: 400px; }
  .intro p {
    font-size: 14px; font-weight: 700; color: var(--navy-text); text-transform: uppercase; line-height: 16.8px;
    margin-bottom: 6px; text-indent: 60px;
  }
  .intro p.small { font-size: 12px; line-height: 14px; text-indent: 0; margin-left: -3px; }
  .login { position: absolute; left: 562px; top: 388px; width: 245px; }
  .login h2 { font-size: 15px; font-weight: 700; color: #222; margin-left: 8px; margin-bottom: 18px; }
  .login label { display: flex; justify-content: space-between; align-items: center; font-size: 15px; color: #222; height: 22px; }
  .login input { width: 166px; height: 21px; border: 1px solid #bcbcbc; }
  .login button {
    margin-top: 18px; font-family: inherit; font-size: 13px; padding: 2px 7px;
    background: linear-gradient(#f4f4f4, #cfcfcf); border: 1px solid #999; text-decoration: underline;
  }
  /* feature rows */
  .feature { position: absolute; left: 0; width: 871px; height: 163px; }
  .feature p {
    position: absolute; left: 72px; top: 52px; width: 450px;
    font-size: 14px; font-weight: 700; color: var(--navy-text); text-transform: uppercase; line-height: 17px;
  }
  .feature-media { position: absolute; left: 548px; top: 17px; width: 255px; height: 136px; overflow: hidden; }
  .feature-photo { width: 255px; height: 112px; }
  .photo-scales { background: linear-gradient(180deg, #8a8c90 0%, #d6d6d4 55%, #3b3b3b 100%); }
  .photo-gavel { background: linear-gradient(160deg, #f1ece6 0%, #c98a4a 45%, #5a2c10 100%); }
  .feature-caption {
    height: 24px; background: var(--navy); color: var(--white); font-weight: 700; font-size: 15px;
    padding-left: 23px; line-height: 24px;
  }
  .read-more {
    position: absolute; right: 8px; top: 5px; background: var(--navy); color: var(--white);
    border: 2px solid var(--pill-border); border-radius: 12px; font-size: 11px; font-weight: 700; padding: 2px 7px;
  }
  /* footer */
  .site-footer { position: absolute; left: 0; top: 1108px; width: 877px; height: 92px; background: var(--footer-bg); }
  .footer-nav a { position: absolute; top: 23px; font-size: 13px; font-weight: 700; color: var(--footer-text); text-decoration: none; white-space: nowrap; }
  .social { position: absolute; left: 686px; top: 14px; display: flex; gap: 8px; }
  .social span { width: 31px; height: 31px; border: 2px solid #e6e6e6; border-radius: 50%; display: flex; align-items: center; justify-content: center; }
  .legal { position: absolute; right: 104px; top: 68px; font-size: 10px; color: var(--footer-text); white-space: nowrap; }
</style>
</head>
<body>
<div class="page">
  <header class="site-header">
    <div class="brand">Harwood &amp; Beale LLP</div>
    <nav class="main-nav">
      <a class="current" href="#" style="left:253px;width:61px">HOME</a>
      <a href="#" style="left:343px;width:63px">NEWS</a>
      <a href="#" style="left:436px;width:72px">SERVICE</a>
      <a href="#" style="left:545px;width:67px">ABOUT</a>
      <a href="#" style="left:642px;width:68px">HELP</a>
      <a href="#" style="left:737px;width:117px">CONTACT US</a>
    </nav>
  </header>
  <div class="band" style="top:86px;height:8px"></div>

  <div class="portrait" role="img" aria-label="Photo of a partner in a dark suit"></div>
  <div class="hero-banner">Harwood &amp; Beale LLP</div>

  <h1 class="tagline">You've come to the right place.</h1>
  <div class="intro">
    <p>Lorem Ipsum is simply dummy text of the printing and typesetting industry. Lorem Ipsum has been the industry's standard dummy text ever since the 1500</p>
    <p>Lorem Ipsum is simply dummy text of the printing and typesetting industry. Lorem Ipsum has been the industry's standard dummy text ever since the 1500</p>
    <p class="small">Lorem Ipsum is simply dummy text of the printing and typesetting industry. Lorem Ipsum has been the industry's standard dummy text ever since the 1500</p>
  </div>

  <form class="login">
    <h2>Customer Login</h2>
    <label>Username <input type="text"></label>
    <label>Password <input type="password"></label>
    <button type="button">Login</button>
  </form>

  <div class="band" style="top:588px;height:9px"></div>

  <section class="feature" style="top:597px">
    <p>Lorem Ipsum is simply dummy text of the printing and typesetting industry. Lorem Ipsum has been the industry's standard dummy text ever since the 1500</p>
    <div class="feature-media">
      <div class="feature-photo photo-scales" role="img" aria-label="Photo of scales of justice against a cloudy sky"></div>
      <div class="feature-caption">LOREM IPSUM</div>
      <span class="read-more">READ MORE</span>
    </div>
  </section>
  <div class="band" style="top:760px;height:10px"></div>

  <section class="feature" style="top:770px">
    <p>Lorem Ipsum is simply dummy text of the printing and typesetting industry. Lorem Ipsum has been the industry's standard dummy text ever since the 1500</p>
    <div class="feature-media">
      <div class="feature-photo photo-gavel" role="img" aria-label="Photo of a wooden gavel and brass scales"></div>
      <div class="feature-caption">LOREM IPSUM</div>
      <span class="read-more">READ MORE</span>
    </div>
  </section>
  <div class="band" style="top:933px;height:9px"></div>

  <section class="feature" style="top:942px">
    <p>Lorem Ipsum is simply dummy text of the printing and typesetting industry. Lorem Ipsum has been the industry's standard dummy text ever since the 1500</p>
    <div class="feature-media">
      <div class="feature-photo photo-scales" role="img" aria-label="Photo of scales of justice against a cloudy sky"></div>
      <div class="feature-caption">LOREM IPSUM</div>
      <span class="read-more">READ MORE</span>
    </div>
  </section>

  <footer class="site-footer">
    <nav class="footer-nav">
      <a href="#" style="left:41px">HOME</a>
      <a href="#" style="left:148px">NEWS</a>
      <a href="#" style="left:265px">SERVICE</a>
      <a href="#" style="left:384px">ABOUT</a>
      <a href="#" style="left:502px">HELP</a>
      <a href="#" style="left:592px">CONTACT US</a>
    </nav>
    <div class="social">
      <span><svg width="16" height="12" viewBox="0 0 16 12"><rect x="1" y="1" width="14" height="10" fill="none" stroke="#e6e6e6" stroke-width="1.6"/><path d="M1 1l7 6 7-6" fill="none" stroke="#e6e6e6" stroke-width="1.6"/></svg></span>
      <span></span>
      <span></span>
    </div>
    <div class="legal">Privacy Policy &nbsp;|&nbsp; Terms and Conditions &nbsp;|&nbsp; © Harwood &amp; Beale 2014</div>
  </footer>
</div>
</body>
</html>
```